Redesign BrightCoinDesk.info

We are unhappy with the design and layout of our current site www.BrightCoinDesk.info
We would like the following pages redesigned using a consistent style.
http://www.brightcoindesk.info/
http://www.brightcoindesk.info/live_forex_signals.php
http://www.brightcoindesk.info/forex-signal/71/TQ-Overdrive.html
http://www.brightcoindesk.info/broker_rebates.php
http://www.brightcoindesk.info/contact.php
Ideally we would also like the contractor to be able to code it into HTML.
We currently like our colour scheme of black, blue and grey.
Updates
We would like to consider a logo redesign. We're happy to pay a $30 bonus for a new logo.
Target Market(s)
80% males between 25 and 50 years old
Industry/Entity Type
Contractor

```html
<!DOCTYPE html>
<html lang="en">
<head>
<meta charset="utf-8">
<title>BrightCoinDesk.info</title>
<link href="https://fonts.googleapis.com/css2?family=Arimo:wght@400;700&display=swap" rel="stylesheet">
<style>
:root{
  --dark:#2f2f2f;
  --dark2:#3d3d3d;
  --blue:#1a84d6;
  --blue-dark:#0f5fae;
  --link:#0b62b8;
  --text:#333;
  --muted:#555;
  --grey-bg:#ececec;
  --card:#f6f6f6;
  --line:#d6d6d6;
}
*{box-sizing:border-box;margin:0;padding:0}
html,body{width:932px;height:1200px;overflow:hidden}
body{position:relative;font-family:"Arimo",Arial,sans-serif;color:var(--text);background:#fff;font-size:11px}
.abs{position:absolute}
a{color:inherit;text-decoration:none}

/* header */
.site-header{left:0;top:0;width:932px;height:102px;background:linear-gradient(#3a3a3a,#2b2b2b)}
.brand{left:70px;top:20px;display:flex;align-items:center;gap:8px}
.brand-mark{width:50px;height:50px;background:#8a8a8a}
.brand-name{font-size:24px;font-weight:700;color:#dcdcdc;letter-spacing:.5px}
.top-nav{right:70px;top:18px;display:flex;gap:10px;color:#e8e8e8;font-size:11.5px}
.top-nav .sep{color:#888}
.search{left:584px;top:50px;width:132px;height:22px;background:#fff;border:1px solid #ccc;font-size:9px;color:#444;padding:5px 10px}
.search svg{position:absolute;right:7px;top:4px}
.account{left:723px;top:50px;height:22px;display:flex;font-size:9px}
.account .register{background:var(--blue-dark);color:#fff;padding:5px 9px 0 24px;width:66px;position:relative}
.account .login{background:#fff;color:#444;padding:5px 8px 0 22px;width:73px;position:relative}

/* main nav */
.main-nav{left:0;top:102px;width:932px;height:43px;background:linear-gradient(#2a96e6,#1475c6);border-top:1px solid #4aaaf0}
.main-nav ul{list-style:none;display:flex;position:absolute;left:70px;top:0;height:43px;border-left:1px solid #1266b0}
.main-nav li{height:42px;line-height:42px;color:#fff;font-weight:700;font-size:11.5px;padding:0 13px;border-right:1px solid #1266b0}
.main-nav li.active{background:var(--blue-dark);padding:0 18px}

/* hero band */
.hero-band{left:0;top:145px;width:932px;height:415px;background:var(--grey-bg)}
.slider{left:70px;top:155px;width:792px;height:284px;background:#fff;box-shadow:0 8px 10px -6px rgba(0,0,0,.35)}
.slide-art{left:75px;top:162px;width:780px;height:270px;background:linear-gradient(160deg,#2b6cc4 0%,#5d9ae0 45%,#1c4f9c 100%)}
.slide-arrow{top:280px;width:32px;height:32px;border-radius:50%;background:rgba(235,240,250,.85)}
.caption{left:88px;top:376px;width:750px;height:47px;background:rgba(10,10,10,.88);color:#fff}
.caption h2{position:absolute;left:18px;top:14px;font-size:17px}
.enter-btn{position:absolute;left:272px;top:7px;width:148px;height:32px;background:linear-gradient(#a9a9a9,#7d7d7d);font-size:16px;font-weight:700;color:#fff;padding:7px 14px}
.caption p{position:absolute;left:469px;top:10px;width:270px;font-size:10px;line-height:14px}
.quote{left:70px;top:484px;width:792px;text-align:center;font-size:12.5px;color:#222}
.quote .mark{position:absolute;top:-2px;font-size:22px;font-weight:700;color:#666}
.author{left:0;top:508px;width:932px;text-align:center;font-size:12.5px;font-weight:700;color:var(--link)}
.stars{left:435px;top:529px;display:flex;gap:1px}

/* welcome */
.welcome{left:70px;top:582px;width:558px}
.welcome h1{font-size:17px;color:var(--link);margin-bottom:8px}
.welcome p{font-size:10px;line-height:18px;color:var(--text);text-align:justify;margin-bottom:6px}
.welcome .more{color:var(--link)}
.rule{left:70px;top:737px;width:558px;height:1px;background:var(--line)}
.feature{top:763px;width:177px;height:137px;background:var(--card);border:1px solid #e2e2e2;text-align:center;box-shadow:0 1px 2px rgba(0,0,0,.08)}
.feature .icon{margin:-8px auto 0;width:40px;height:44px;border-radius:6px}
.feature h3{font-size:13.5px;color:var(--link);margin:12px 0 8px}
.feature h3 span{color:#444}
.feature p{font-size:9.3px;line-height:16px;color:var(--muted);padding:0 10px}

.promo{left:645px;top:585px;width:217px;height:135px;background:linear-gradient(#555,#303030);border-radius:3px;text-align:center;color:#fff}
.promo h3{font-size:13px;line-height:19.5px;margin:17px 8px 12px}
.promo .btn{display:inline-block;background:linear-gradient(#2a96e6,#1070c4);padding:8px 10px;font-size:11.5px;font-weight:700;border:1px solid #0e5ea8}
.signals{left:645px;top:727px;width:217px;height:173px;background:linear-gradient(#555,#303030);border-radius:3px}
.signals h3{color:#fff;font-size:16px;position:absolute;left:15px;top:9px}
.signals ul{position:absolute;left:4px;top:36px;width:209px;height:133px;background:#fff;list-style:none;padding:9px 0 0 15px}
.signals li{font-size:10.3px;line-height:15px;margin-bottom:11px;color:#222}
.signals li b{color:var(--link)}

/* bottom widgets */
.widgets{left:0;top:912px;width:932px;height:160px;background:var(--grey-bg)}
.widget{top:922px;width:256px;height:136px;background:#fff;box-shadow:0 1px 3px rgba(0,0,0,.15)}
.widget .w-icon{position:absolute;left:16px;top:18px;width:32px;height:26px}
.widget h3{position:absolute;left:58px;top:18px;font-size:16.5px;font-weight:400;color:var(--blue)}
.widget .thumb{position:absolute;left:18px;top:59px;width:28px;height:28px}
.widget p{position:absolute;left:54px;top:58px;width:192px;font-size:9.3px;line-height:16.2px;color:var(--muted)}
.widget p a{color:var(--blue-dark)}

/* footer */
.site-footer{left:0;top:1072px;width:932px;height:128px;background:var(--dark)}
.foot-links{position:absolute;left:70px;top:20px;width:792px;text-align:center;font-size:11px;color:#ddd;line-height:21px}
.foot-links .sep{margin:0 7px;color:#bbb}
.foot-rule{position:absolute;left:70px;top:74px;width:792px;height:1px;background:#555}
.copyright{position:absolute;left:70px;top:92px;font-size:10.5px;color:#ddd;word-spacing:1px}
.social{position:absolute;top:91px;width:18px;height:18px;border-radius:3px}
</style>
</head>
<body>

<header class="site-header abs">
  <div class="brand abs"><span class="brand-mark"></span><span class="brand-name">BrightCoinDesk.info</span></div>
  <nav class="top-nav abs"><a>Home</a><span class="sep">::</span><a>About Us</a><span class="sep">::</span><a>Forum</a><span class="sep">::</span><a>Contact Us</a></nav>
  <div class="search abs">Search
    <svg width="14" height="14" viewBox="0 0 14 14"><circle cx="5.5" cy="5.5" r="4" fill="none" stroke="#222" stroke-width="2"/><line x1="8.5" y1="8.5" x2="13" y2="13" stroke="#222" stroke-width="2.5"/></svg>
  </div>
  <div class="account abs">
    <a class="register"><svg class="abs" style="left:9px;top:5px" width="9" height="11" viewBox="0 0 9 11"><rect x="0" y="4" width="9" height="7" fill="#fff"/><path d="M2 4V2.5a2.5 2.5 0 0 1 5 0V4" fill="none" stroke="#fff" stroke-width="1.5"/></svg>Regster</a>
    <a class="login"><svg class="abs" style="left:8px;top:5px" width="10" height="11" viewBox="0 0 10 11"><circle cx="5" cy="3" r="2.8" fill="#555"/><rect x="0" y="7" width="10" height="4" fill="#555"/></svg>Log in <svg width="7" height="5" viewBox="0 0 7 5" style="margin-left:6px"><path d="M0 0h7L3.5 5z" fill="#555"/></svg></a>
  </div>
</header>

<nav class="main-nav abs">
  <ul>
    <li class="active">Enter Trading Room</li>
    <li>Control Panel</li>
    <li>Forex Advice</li>
    <li>Live Forex Trading Signals</li>
    <li>Broker Reviews</li>
    <li>Become a Team Trader</li>
  </ul>
</nav>

<section class="hero-band abs"></section>
<div class="slider abs"></div>
<div class="slide-art abs" role="img" aria-label="Glass office towers seen from below against a blue sky"></div>
<div class="slide-arrow abs" style="left:84px"><svg width="32" height="32" viewBox="0 0 32 32"><path d="M18 10l-6 6 6 6" fill="none" stroke="#8aa" stroke-width="1.5"/></svg></div>
<div class="slide-arrow abs" style="left:813px"><svg width="32" height="32" viewBox="0 0 32 32"><path d="M14 10l6 6-6 6" fill="none" stroke="#8aa" stroke-width="1.5"/></svg></div>
<div class="caption abs">
  <h2>Follow Professional Traders</h2>
  <a class="enter-btn">ENTER NOW &raquo;</a>
  <p>Did you know you can copy trades automatically into your account using our special software?</p>
</div>
<blockquote class="quote abs"><span class="mark" style="left:0">&ldquo;</span>I just bought a new TV and Dishwasher with the money I've made from this site. I couldn't have done it without you, thanks guys!<span class="mark" style="right:0">&rdquo;</span></blockquote>
<div class="author abs">Rexford - Australia</div>
<div class="stars abs">
  <svg width="60" height="12" viewBox="0 0 60 12">
    <g fill="#3a6fc0"><path id="st" d="M6 0l1.8 3.9 4.2.4-3.2 2.8 1 4.1L6 9.1 2.2 11.2l1-4.1L0 4.3l4.2-.4z"/><use href="#st" x="12"/><use href="#st" x="24"/><use href="#st" x="36"/></g>
    <use href="#st" x="48" fill="#999"/>
  </svg>
</div>

<section class="welcome abs">
  <h1>Welcome to our site</h1>
  <p>My name is Dan Whitaker and I'm the owner and founder of BrightCoinDesk.info. I created this site to reach out to all the retail forex traders in the world who are struggling to trade profitably.Here we give you the opportunity to connect with full time, professional forex traders and copy their signals inside our free forex trading room.</p>
  <p>I have extensive experience trading the forex market, however my true passion lies in building relationships with other talented and experienced traders across the globe and then benefiting from the profitable trading opportunities they identify by copying their trades. <a class="more">More...</a></p>
</section>
<div class="rule abs"></div>

<article class="feature abs" style="left:70px">
  <div class="icon" style="background:#4a5a6e" role="img" aria-label="Businessman figure"></div>
  <h3>Who Are We?</h3>
  <p>We are traders who are growing substantial wealth through trading Forex (Foreign Exchange).</p>
</article>
<article class="feature abs" style="left:260px">
  <div class="icon" style="background:radial-gradient(#3a8fe0,#5d6c7c)" role="img" aria-label="Blue gear"></div>
  <h3>How Do We Do It?</h3>
  <p>We leverage off successful strate-gies and systems found across the internet to find the few...</p>
</article>
<article class="feature abs" style="left:451px">
  <div class="icon" style="background:#e8a79a" role="img" aria-label="Piggy bank"></div>
  <h3>Is It Free? - <span>YES!</span></h3>
  <p>The trading signals are displayed live within the Forex Trading Room completely free of charge.</p>
</article>

<aside class="promo abs">
  <h3>Are you a total Newbie? Let us show you how to get start trading forex profitably today!</h3>
  <a class="btn">Click here to know more</a>
</aside>
<aside class="signals abs">
  <h3>Latest Signal</h3>
  <ul>
    <li><b>SELL - USDJPY</b><br>Open Price: 98.0990 &nbsp;::&nbsp; 3 hours ago</li>
    <li><b>SELL - USDJPY</b><br>Open Price: 98.0990 &nbsp;::&nbsp; 3 hours ago</li>
    <li><b>SELL - USDJPY</b><br>Open Price: 98.0990 &nbsp;::&nbsp; 3 hours ago</li>
  </ul>
</aside>

<section class="widgets abs"></section>
<article class="widget abs" style="left:70px">
  <svg class="w-icon" viewBox="0 0 32 26"><circle cx="16" cy="13" r="10" fill="#3aa7dc"/></svg>
  <h3 style="left:58px">Social Feed</h3>
  <div class="thumb" style="background:#3aa7dc;top:62px;width:26px;height:26px"></div>
  <p><a>TQ Overdrive is continuing to dominate. Make sure you sign up soon if you want to follow this amazing trader. Subs cut off at 500!</a> &nbsp;2 days ago</p>
</article>
<article class="widget abs" style="left:338px">
  <div class="w-icon" style="background:linear-gradient(#eee,#bbb);width:30px;height:28px" role="img" aria-label="Newspaper icon"></div>
  <h3 style="left:58px">Latest News</h3>
  <div class="thumb" style="background:linear-gradient(#f2f2f2,#c8c8c8);border:1px solid #aaa;height:26px" role="img" aria-label="News thumbnail"></div>
  <p><a>Watch Me Turn $30k into $300k!</a><br>I'm using $30k of my own funds to follow the signals at BrightCoinDesk to show everyone how easy it is to make...</p>
</article>
<article class="widget abs" style="left:606px">
  <div class="w-icon" style="background:radial-gradient(circle at 40% 40%,#5fc1e8,#5cab3c);border-radius:50%;width:28px;height:28px" role="img" aria-label="Speech bubbles icon"></div>
  <h3 style="left:58px">Latest Forum</h3>
  <div class="thumb" style="background:#ddd;border:1px solid #ccc" role="img" aria-label="Member avatar placeholder"></div>
  <p><a>General Forex</a><br>We generate the monthly profit reports for all the signals provided through BrightCoin-Desk in this forum.</p>
</article>

<footer class="site-footer abs">
  <div class="foot-links">
    Home<span class="sep">|</span>Enter Trading Room<span class="sep">|</span>Control Panel<span class="sep">|</span>Forex Advice<span class="sep">|</span>Live Forex Trading Signals<span class="sep">|</span>Broker Reviews<span class="sep">|</span>Become a Team Trader<span class="sep">|</span>About us<br>
    Forums<span class="sep">|</span>Contact us<span class="sep">|</span>Terms and conditions<span class="sep">|</span>Privacy policy
  </div>
  <div class="foot-rule"></div>
  <div class="copyright">Copyright &copy; 2013 &nbsp;&nbsp; www.BrightCoinDesk.info &nbsp;&nbsp; All rights reserved.</div>
  <div class="social" style="left:819px;background:#3b5a9a"></div>
  <div class="social" style="left:844px;background:#3fb2e6"></div>
</footer>

</body>
</html>
```